Calm Harbor Blueprint

I need a on page electronic flyer for this coaching program. I want a silhouette to accompany the case the copy starts with. I have the copy written but need it put together in a striking way.

Target Market(s)

towards higher net worth individuals

Industry/Entity Type

Electronic

```html
<!DOCTYPE html>
<html lang="en">
<head>
<meta charset="utf-8">
<title>Calm Harbor Blueprint</title>
<link href="https://fonts.googleapis.com/css2?family=Archivo+Black&family=Arimo:wght@400;700&family=Arvo:wght@700&display=swap" rel="stylesheet">
<style>
  :root {
    --ink: #111111;
    --navy: #1b2a4a;
    --blue: #1a7fc4;
    --red: #e02626;
    --orange: #f08a1c;
    --yellow: #f6c21b;
    --green: #7ab540;
    --paper: #ffffff;
  }
  * { margin: 0; padding: 0; box-sizing: border-box; }
  html, body { width: 928px; height: 1200px; overflow: hidden; background: var(--paper); }
  .flyer { position: relative; width: 928px; height: 1200px; font-family: "Arimo", Arial, sans-serif; color: var(--ink); }

  .headline { position: absolute; left: 42px; top: 18px; width: 860px; font-family: "Archivo Black", "Arial Black", sans-serif; font-size: 35px; line-height: 44px; letter-spacing: 0.2px; }
  .subhead { position: absolute; left: 78px; top: 116px; font-weight: 700; font-size: 26px; line-height: 32px; }

  .band { position: absolute; left: 42px; width: 842px; display: flex; }
  .band span { display: block; height: 100%; }
  .band-top { top: 194px; height: 13px; }
  .band-mid { top: 438px; height: 7px; }
  .band-low { top: 612px; height: 13px; }
  .band-green { top: 832px; height: 13px; width: 650px; background: var(--green); }

  .story { position: absolute; left: 42px; top: 220px; width: 842px; display: grid; grid-template-columns: 1fr 1fr; column-gap: 28px; font-size: 15px; line-height: 18px; text-align: justify; }
  .story p { margin-bottom: 9px; }

  .question { position: absolute; left: 42px; top: 456px; font-weight: 700; font-size: 20px; line-height: 24px; }
  .process { position: absolute; left: 180px; top: 490px; font-size: 15px; line-height: 21px; }
  .process-intro { font-weight: 700; margin-bottom: 4px; }
  .process ul { list-style: none; padding-left: 18px; }
  .process li { position: relative; padding-left: 18px; }
  .process li::before { content: ""; position: absolute; left: 0; top: 8px; width: 6px; height: 6px; border-radius: 50%; background: var(--ink); }

  .method { position: absolute; left: 42px; top: 640px; font-size: 15px; line-height: 18px; }
  .method p { margin-bottom: 9px; }
  .method .wide { width: 842px; }
  .method .narrow { width: 620px; }

  .brand-mark { position: absolute; left: 688px; top: 720px; width: 216px; height: 216px; border-radius: 50%; background: var(--blue); display: flex; align-items: center; justify-content: center; }
  .brand-name { font-weight: 700; font-size: 30px; color: var(--paper); text-align: center; line-height: 34px; }

  .silhouette { position: absolute; left: 96px; top: 866px; width: 200px; height: 200px; }
  .case-label { position: absolute; left: 106px; top: 1016px; width: 180px; text-align: center; color: var(--paper); font-family: "Arvo", serif; font-weight: 700; font-size: 16px; line-height: 20px; }

  .program { position: absolute; left: 362px; top: 878px; font-family: "Arvo", Georgia, serif; font-weight: 700; font-size: 25px; line-height: 37px; }
  .program .lead { color: var(--navy); }
  .program .blue { color: var(--blue); }
  .program .red { color: var(--red); }
  .program .orange { color: var(--orange); }
  .program .green { color: var(--green); }

  .bio { position: absolute; left: 0; top: 1092px; width: 928px; text-align: center; font-size: 16px; line-height: 21px; }
</style>
</head>
<body>
<main class="flyer">
  <h1 class="headline">Sometimes the best financial advice<br>isn't about numbers...</h1>
  <h2 class="subhead">Calm Harbor Blueprint:<br>From Financial Worries to Wealth Satisfaction</h2>

  <div class="band band-top">
    <span style="width:60%;background:var(--blue)"></span>
    <span style="width:14%;background:var(--red)"></span>
    <span style="width:13%;background:var(--orange)"></span>
    <span style="width:13%;background:var(--yellow)"></span>
  </div>

  <section class="story">
    <div>
      <p>A 49 year old attorney, Mark was used to success and rising net worth. But with huge losses in the market crash, layoffs at his firm, his kids heading for college and the stagnant economy stretching ahead, his usual optimism is gone.</p>
      <p>With his anxiety growing, Mark doubts his own decision making ability. His confidence slipping, he stopped opening his financial statements and could barely speak to his financial advisor. He thought if his advisor said “hang in there” one more time, he just might blow up.</p>
    </div>
    <div>
      <p>Yet Mark felt too embarrassed to talk about his deep worries, even with his wife. It seemed like all he could do was pour another glass of wine and suffer in isolation.</p>
      <p>If you're like Mark, you're afraid and alone with plenty of company. In a September 2009 National Wellbeing Council poll, 80 percent reported the economy is causing significant stress, up from 66 percent from the previous April. The Restful Nights Institute found said 27 percent of people surveyed had sleeplessness because of economic anxiety.</p>
    </div>
  </section>

  <div class="band band-mid">
    <span style="width:40%;background:var(--red)"></span>
    <span style="width:20%;background:var(--orange)"></span>
    <span style="width:20%;background:var(--yellow)"></span>
    <span style="width:20%;background:var(--blue)"></span>
  </div>

  <h3 class="question">How can you take control of these worries and get back to enjoying your life?</h3>
  <div class="process">
    <p class="process-intro">In this 5 session coaching process you will:</p>
    <ul>
      <li>Learn a decision making tool to make choices that truly serve your needs</li>
      <li>Clarify and more fully engage with your purpose and passions</li>
      <li>Improve your relationship with your financial advisor</li>
      <li>Feel more in control and confident in your financial life</li>
    </ul>
  </div>

  <div class="band band-low">
    <span style="width:55%;background:var(--red)"></span>
    <span style="width:25%;background:var(--orange)"></span>
    <span style="width:20%;background:var(--yellow)"></span>
  </div>

  <section class="method">
    <p class="wide">This process guides you to step back and understand the source of your financial worry—your unique story about the meaning of money. Your money story drives your emotions and decision making—for better and worse. You'll learn a decision making tool for more conscious, effective and satisfying financial and life decisions.</p>
    <p class="narrow">You'll also examine your core values and strengths—what really matters most to you and how you work at your best. When you use your money and your core strengths to pursue your highest aspirations, life and wealth become balanced. As you commit more fully to your mission and passions, satisfaction grows and money worries melt away.</p>
  </section>

  <div class="band band-green"></div>

  <div class="brand-mark">
    <p class="brand-name">HARBOR<br>CIRCLE</p>
  </div>

  <svg class="silhouette" viewBox="0 0 200 200" role="img" aria-label="Dark silhouette of a man's head and shoulders representing the case study client">
    <rect x="0" y="0" width="200" height="200" fill="var(--ink)"/>
  </svg>
  <p class="case-label">“Marcus”<br>Brookhaven, PA</p>

  <div class="program">
    <p class="lead">A Six Week Program to</p>
    <p class="blue">Reduce Stress</p>
    <p class="red">Improve Performance</p>
    <p class="orange">Restore Control</p>
    <p class="green">$995 Money Back Guarantee</p>
  </div>

  <footer class="bio">
    <p>Dana Whitlow, Ph.D. is a psychologist with 30 years of experience treating anxiety and stress.</p>
    <p>She is co-founder and facilitator of Harbor Circle, a peer learning group for high net worth investors.</p>
    <p>For more information, call 555-014-2290. dwhitlow@example.com</p>
  </footer>
</main>
</body>
</html>
```